Furline Rescue Website design in word press

Develop great looking website home page with basic menus in Word Press. We already have a logo, so no need to re-invent that.

Target Market(s)

donors, animal owners, emergency services.

Number of Pages Required

1 page

Font styles to use
Sans Serif

Colors
ec1f27
000000
ffffff
959595

Requirements
Must have
• Fresh design in Word Press, neutral (i.e. not American looking), uses red, black and white as core colours. Needs to have menu options for about us, join us, help us, FAQs, contact us etc. Looking for a smart, modern, professional looking home page, that we can easily add pages/menu's/widgets to. Include social media buttons for facebook, twitter etc.
Nice to have
• Images (could be in colour shades) of animals in disaster i.e. search royalty free Hurricane Velmorra, Hurrican Dostrel.
Should not have
• Images that breach copyright.

```html
<!DOCTYPE html>
<html lang="en">
<head>
<meta charset="utf-8">
<title>Furline Rescue – Home</title>
<link href="https://fonts.googleapis.com/css2?family=Lato:wght@400;700;900&family=Open+Sans:wght@400;600;700&display=swap" rel="stylesheet">
<style>
:root{
  --red:#ec1f27;
  --black:#000000;
  --white:#ffffff;
  --grey:#959595;
  --ink:#222222;
  --body:#666666;
  --panel:#f2f2f2;
  --line:#d6d6d6;
}
*{box-sizing:border-box;margin:0;padding:0}
html,body{width:1200px;height:3495px;overflow:hidden;background:var(--white)}
body{position:relative;font-family:'Open Sans',Arial,sans-serif;color:var(--ink)}
.abs{position:absolute}
h2.section-title{position:absolute;left:0;width:1200px;text-align:center;font-family:'Lato',Arial,sans-serif;font-weight:700;font-size:38px;color:var(--black);letter-spacing:.5px}

/* header */
.site-header{position:absolute;left:0;top:0;width:1200px;height:106px;background:var(--white);box-shadow:0 2px 6px rgba(0,0,0,.12);z-index:2}
.brand{position:absolute;left:98px;top:12px;display:flex;align-items:center;gap:12px}
.brand-dot{width:76px;height:76px;border-radius:50%;background:var(--red)}
.brand-name{font-family:'Open Sans',sans-serif;font-weight:700;font-size:17px;color:var(--red);letter-spacing:.5px}
.cta-row{position:absolute;right:98px;top:10px;display:flex;gap:12px}
.pill{display:inline-block;border:2px solid var(--red);color:var(--red);border-radius:22px;font-weight:700;font-size:14px;padding:8px 22px;background:var(--white)}
.main-nav{position:absolute;right:98px;top:70px;display:flex;gap:26px;font-family:'Open Sans',sans-serif;font-weight:600;font-size:15px;color:var(--black)}
.main-nav .active{color:var(--red)}

/* hero */
.hero{position:absolute;left:0;top:106px;width:1200px;height:519px;background:linear-gradient(180deg,#5e6b4a 0%,#7d7b60 40%,#8b7c5f 70%,#6b5d45 100%)}
.hero-title{position:absolute;left:0;top:92px;width:1200px;text-align:center;font-family:'Lato',sans-serif;font-weight:900;font-size:86px;color:var(--white);letter-spacing:1px}
.hero-tag{position:absolute;left:0;top:195px;width:1200px;text-align:center;font-size:28px;color:var(--white);word-spacing:6px}
.hero-btn{position:absolute;left:515px;top:255px;width:170px;height:56px;border:2px solid var(--white);border-radius:28px;color:var(--white);font-weight:600;font-size:15px;text-align:center;line-height:52px}
.slider-dots{position:absolute;left:565px;top:450px;display:flex;gap:6px}
.slider-dots span{width:12px;height:12px;border-radius:50%;border:2px solid var(--white)}
.slider-dots span.on{background:var(--white)}

/* welcome */
.intro{position:absolute;left:170px;top:774px;width:860px;text-align:center;font-size:13.5px;line-height:24px;color:var(--body)}
.goal{position:absolute;height:126px;border:1.5px solid var(--grey);background:var(--white);display:flex;align-items:center;font-family:'Open Sans',sans-serif;font-weight:600;font-size:16px;line-height:26px;color:var(--ink)}
.goal.left{justify-content:flex-end;text-align:right;padding-right:165px}
.goal.right{padding-left:165px}
.badge{position:absolute;width:130px;height:130px}

/* values */
.values-photo{position:absolute;left:0;top:1305px;width:600px;height:533px;background:linear-gradient(160deg,#4a4a4a,#7a7a76 50%,#3b3b3b)}
.values-panel{position:absolute;left:600px;top:1305px;width:600px;height:533px;background:var(--panel)}
.values-panel h2{position:absolute;left:53px;top:40px;font-family:'Lato',sans-serif;font-weight:700;font-size:36px;color:var(--black)}
.values-list{position:absolute;left:53px;top:103px;width:460px;list-style:none}
.values-list li{position:relative;padding-left:24px;font-size:13px;line-height:19px;color:#444;margin-bottom:15px}
.values-list li svg{position:absolute;left:0;top:2px}
.outline-btn{position:absolute;border:2px solid var(--red);border-radius:26px;color:var(--red);font-weight:700;font-size:15px;text-align:center}

/* blog */
.post{position:absolute;top:2020px;width:325px}
.post-img{width:325px;height:230px}
.post h3{margin-top:34px;font-family:'Open Sans',sans-serif;font-weight:600;font-size:19px;color:var(--black)}
.meta{margin-top:12px;font-size:13px;color:#555;display:flex;align-items:center;gap:6px}
.post p{margin-top:14px;font-size:13.5px;line-height:22px;color:var(--body)}
.more{display:block;margin-top:16px;font-weight:700;font-size:13.5px;color:var(--red)}

/* volunteer */
.volunteer{position:absolute;left:0;top:2558px;width:1200px;height:362px;background:linear-gradient(180deg,#5b5e63 0%,#4a4640 55%,#3a342d 100%)}
.volunteer h2{position:absolute;top:62px;width:1200px;text-align:center;font-family:'Lato',sans-serif;font-weight:700;font-size:34px;color:var(--white)}
.volunteer p{position:absolute;top:125px;left:300px;width:600px;text-align:center;font-size:17px;line-height:28px;color:var(--white);font-weight:600}
.volunteer .book{position:absolute;left:508px;top:215px;width:184px;height:58px;border:2px solid var(--white);border-radius:29px;color:var(--white);font-weight:700;font-size:16px;text-align:center;line-height:54px}

/* contact */
.sub-head{position:absolute;font-family:'Open Sans',sans-serif;font-size:19px;color:var(--ink)}
.field{position:absolute;border:1px solid #bbb;font-size:11px;color:#555;padding:7px 10px}
.submit{position:absolute;left:626px;top:3331px;width:102px;height:42px;border-radius:21px;background:var(--red);color:var(--white);font-weight:700;font-size:14px;text-align:center;line-height:42px}
.info-row{position:absolute;left:783px;display:flex;align-items:center;gap:22px;font-size:12.5px;line-height:20px;color:#444}
.info-icon{width:34px;height:34px;border-radius:50%;border:1px solid #ddd;display:flex;align-items:center;justify-content:center;flex:none}
.socials{position:absolute;left:783px;top:3335px;display:flex;gap:12px}
.socials span{width:34px;height:34px;border-radius:50%}
.rule{position:absolute;left:98px;top:3413px;width:1006px;height:1px;background:var(--line)}
.copyright{position:absolute;top:3450px;width:1200px;text-align:center;font-size:12px;color:#555}
</style>
</head>
<body>

<header class="site-header">
  <div class="brand"><span class="brand-dot"></span><span class="brand-name">FURLINE RESCUE</span></div>
  <div class="cta-row">
    <span class="pill">DONATE NOW!</span>
    <span class="pill">ADD TO PLAN</span>
    <span class="pill">HELP FUNDRAISE</span>
  </div>
  <nav class="main-nav">
    <span class="active">HOME</span><span>ABOUT US</span><span>JOIN US</span><span>HELP US</span><span>FAQS</span><span>CONTACT US</span>
    <svg width="16" height="16" viewBox="0 0 16 16" style="margin-top:3px"><circle cx="6.5" cy="6.5" r="4.5" fill="none" stroke="#000" stroke-width="2"/><line x1="10" y1="10" x2="14" y2="14" stroke="#000" stroke-width="2.4"/></svg>
  </nav>
</header>

<section class="hero" role="img" aria-label="Volunteers wading through a flooded street carrying rescued animals">
  <div class="hero-title">FURLINE RESCUE</div>
  <div class="hero-tag">Evacuate | Shelter | Reunite</div>
  <div class="hero-btn">GET INVOLVED!</div>
  <div class="slider-dots"><span class="on"></span><span></span><span></span><span></span></div>
</section>

<h2 class="section-title" style="top:702px">WELCOME TO FURLINE RESCUE</h2>
<p class="intro">Formed in 2018, following the devastating Marrowvale flood the year prior that saw over 1,000 animals left behind in need of rescue, Furline Rescue New Zealand (Kararehe Haumaru) is a charity comprised of volunteers including veterinary and disaster response professionals, to ensure the needs of animals are better served in future emergencies.</p>

<div class="goal left" style="left:98px;top:907px;width:470px">An animal-inclusive and disaster<br>resilient New Zealand.</div>
<div class="goal right" style="left:627px;top:907px;width:477px">To address the significant animal<br>welfare emergency management<br>capability gap</div>
<div class="goal left" style="left:98px;top:1070px;width:470px">To protect disaster affected animals<br>in partnership with the community</div>
<div class="goal right" style="left:627px;top:1070px;width:477px">To provide local response to support<br>animal evacuation, sheltering and<br>reunification</div>

<svg class="badge" style="left:445px;top:905px" viewBox="0 0 130 130"><circle cx="65" cy="65" r="58" fill="#fff" stroke="#959595" stroke-width="5"/><circle cx="65" cy="65" r="40" fill="#fff" stroke="#959595" stroke-width="3"/><path d="M65 84 L45 64 A11 11 0 0 1 65 50 A11 11 0 0 1 85 64 Z" fill="#ec1f27"/></svg>
<svg class="badge" style="left:625px;top:905px" viewBox="0 0 130 130"><circle cx="65" cy="65" r="58" fill="#fff" stroke="#959595" stroke-width="5"/><circle cx="65" cy="65" r="40" fill="#fff" stroke="#959595" stroke-width="3"/><circle cx="65" cy="65" r="22" fill="none" stroke="#ec1f27" stroke-width="5"/><path d="M65 53 V66 H74" fill="none" stroke="#ec1f27" stroke-width="4"/></svg>
<svg class="badge" style="left:445px;top:1068px" viewBox="0 0 130 130"><circle cx="65" cy="65" r="58" fill="#fff" stroke="#959595" stroke-width="5"/><circle cx="65" cy="65" r="40" fill="#fff" stroke="#959595" stroke-width="3"/><circle cx="65" cy="53" r="7" fill="#ec1f27"/><circle cx="49" cy="60" r="6" fill="#ec1f27"/><circle cx="81" cy="60" r="6" fill="#ec1f27"/><path d="M52 82 a13 13 0 0 1 26 0 Z M38 80 a11 11 0 0 1 20 -6 L56 80Z M92 80 a11 11 0 0 0 -20 -6 L74 80Z" fill="#ec1f27"/></svg>
<svg class="badge" style="left:625px;top:1068px" viewBox="0 0 130 130"><circle cx="65" cy="65" r="58" fill="#fff" stroke="#959595" stroke-width="5"/><circle cx="65" cy="65" r="40" fill="#fff" stroke="#959595" stroke-width="3"/><path d="M45 72 V64 a20 20 0 0 1 40 0 V72" fill="none" stroke="#ec1f27" stroke-width="5"/><rect x="41" y="66" width="10" height="16" rx="3" fill="#ec1f27"/><rect x="79" y="66" width="10" height="16" rx="3" fill="#ec1f27"/></svg>

<div class="values-photo" role="img" aria-label="Rescuer carrying two small dogs through flood water among evacuees"></div>
<section class="values-panel">
  <h2>OUR VALUES</h2>
  <ul class="values-list">
    <li><svg width="13" height="13" viewBox="0 0 13 13"><circle cx="6.5" cy="6.5" r="6.5" fill="#ec1f27"/><path d="M3.5 6.8 L5.7 9 L9.6 4.6" fill="none" stroke="#fff" stroke-width="1.8"/></svg>We are the leading voice for all animals affected by disaster</li>
    <li><svg width="13" height="13" viewBox="0 0 13 13"><circle cx="6.5" cy="6.5" r="6.5" fill="#ec1f27"/><path d="M3.5 6.8 L5.7 9 L9.6 4.6" fill="none" stroke="#fff" stroke-width="1.8"/></svg>We act to do the right thing for the animals in a disaster management context</li>
    <li><svg width="13" height="13" viewBox="0 0 13 13"><circle cx="6.5" cy="6.5" r="6.5" fill="#ec1f27"/><path d="M3.5 6.8 L5.7 9 L9.6 4.6" fill="none" stroke="#fff" stroke-width="1.8"/></svg>We develop local capacity to create animal inclusive community resilience</li>
    <li><svg width="13" height="13" viewBox="0 0 13 13"><circle cx="6.5" cy="6.5" r="6.5" fill="#ec1f27"/><path d="M3.5 6.8 L5.7 9 L9.6 4.6" fill="none" stroke="#fff" stroke-width="1.8"/></svg>We hold to account those with responsibilities to protect animals from disaster</li>
    <li><svg width="13" height="13" viewBox="0 0 13 13"><circle cx="6.5" cy="6.5" r="6.5" fill="#ec1f27"/><path d="M3.5 6.8 L5.7 9 L9.6 4.6" fill="none" stroke="#fff" stroke-width="1.8"/></svg>We inform our position and activities using best practice and scientific knowledge</li>
    <li><svg width="13" height="13" viewBox="0 0 13 13"><circle cx="6.5" cy="6.5" r="6.5" fill="#ec1f27"/><path d="M3.5 6.8 L5.7 9 L9.6 4.6" fill="none" stroke="#fff" stroke-width="1.8"/></svg>We do not advocate on non-disaster related animal welfare issues.</li>
  </ul>
  <div class="outline-btn" style="left:53px;top:438px;width:140px;height:50px;line-height:46px">READ MORE</div>
</section>

<h2 class="section-title" style="top:1922px">OUR BLOG</h2>

<article class="post" style="left:98px">
  <div class="post-img" role="img" aria-label="Rescuers with a large dog in an inflatable boat" style="background:linear-gradient(160deg,#8fa3b3,#5a5f63 55%,#2f3134)"></div>
  <h3>Finibus Bonoret Malorum</h3>
  <div class="meta"><svg width="12" height="12" viewBox="0 0 12 12"><rect x="1" y="2" width="10" height="9" fill="none" stroke="#ec1f27" stroke-width="1.5"/><line x1="1" y1="5" x2="11" y2="5" stroke="#ec1f27" stroke-width="1.5"/></svg>25/09/2017 &nbsp;|&nbsp; <svg width="11" height="12" viewBox="0 0 11 12"><circle cx="5.5" cy="3.5" r="3" fill="#ec1f27"/><path d="M0 12 a5.5 5.5 0 0 1 11 0Z" fill="#ec1f27"/></svg>John</div>
  <p>At vero eos et accusamus et iusto odio dignissimos ducimus qui blanditiis pra esentium voluptatum dele.</p>
  <span class="more">READ MORE</span>
</article>
<article class="post" style="left:440px">
  <div class="post-img" role="img" aria-label="Volunteer comforting an animal among storm debris" style="background:linear-gradient(160deg,#b8ab96,#7a6a58 50%,#3d342b)"></div>
  <h3>Finibus Bonoret Malorum</h3>
  <div class="meta"><svg width="12" height="12" viewBox="0 0 12 12"><rect x="1" y="2" width="10" height="9" fill="none" stroke="#ec1f27" stroke-width="1.5"/><line x1="1" y1="5" x2="11" y2="5" stroke="#ec1f27" stroke-width="1.5"/></svg>25/09/2017 &nbsp;|&nbsp; <svg width="11" height="12" viewBox="0 0 11 12"><circle cx="5.5" cy="3.5" r="3" fill="#ec1f27"/><path d="M0 12 a5.5 5.5 0 0 1 11 0Z" fill="#ec1f27"/></svg>John</div>
  <p>At vero eos et accusamus et iusto odio dignissimos ducimus qui blanditiis pra esentium voluptatum dele.</p>
  <span class="more">READ MORE</span>
</article>
<article class="post" style="left:781px">
  <div class="post-img" role="img" aria-label="Community gathering outside a hall under a blue sky" style="background:linear-gradient(180deg,#2c5bb0 0%,#4a78c4 40%,#2e3a2a 75%,#1d1d1d)"></div>
  <h3>Finibus Bonoret Malorum</h3>
  <div class="meta"><svg width="12" height="12" viewBox="0 0 12 12"><rect x="1" y="2" width="10" height="9" fill="none" stroke="#ec1f27" stroke-width="1.5"/><line x1="1" y1="5" x2="11" y2="5" stroke="#ec1f27" stroke-width="1.5"/></svg>25/09/2017 &nbsp;|&nbsp; <svg width="11" height="12" viewBox="0 0 11 12"><circle cx="5.5" cy="3.5" r="3" fill="#ec1f27"/><path d="M0 12 a5.5 5.5 0 0 1 11 0Z" fill="#ec1f27"/></svg>John</div>
  <p>At vero eos et accusamus et iusto odio dignissimos ducimus qui blanditiis pra esentium voluptatum dele.</p>
  <span class="more">READ MORE</span>
</article>

<section class="volunteer" role="img" aria-label="Storm-damaged houses and debris after a hurricane">
  <h2>WANT TO VOLUNTEER? BOOK YOUR FIRST COURSE</h2>
  <p>Nam libero tempore, cum soluta nobis est eligendi optio cumque nihil impedit quo minus id quod maxime placeat facere possimus, omnis volu</p>
  <div class="book">BOOK NOW!</div>
</section>

<h2 class="section-title" style="top:3002px">CONTACT US</h2>
<div class="sub-head" style="left:98px;top:3078px">Contact form</div>
<div class="field" style="left:98px;top:3143px;width:311px;height:32px">Name :</div>
<div class="field" style="left:418px;top:3143px;width:310px;height:32px">Phone no :</div>
<div class="field" style="left:98px;top:3190px;width:630px;height:30px">Email :</div>
<div class="field" style="left:98px;top:3233px;width:630px;height:80px">Message :</div>
<div class="submit">SUBMIT</div>

<div class="sub-head" style="left:783px;top:3078px">Contact Information</div>
<div class="info-row" style="top:3130px"><span class="info-icon"><svg width="12" height="16" viewBox="0 0 12 16"><path d="M6 16 C2 10 0 8 0 6 a6 6 0 0 1 12 0 C12 8 10 10 6 16Z" fill="#ec1f27"/><circle cx="6" cy="6" r="2.2" fill="#fff"/></svg></span><span>Nam libero tempore, cum soluta no<br>bis est eligendi optio</span></div>
<div class="info-row" style="top:3193px"><span class="info-icon"><svg width="14" height="14" viewBox="0 0 14 14"><path d="M3 0 L5.5 3.5 L4 5.5 C5 7.5 6.5 9 8.5 10 L10.5 8.5 L14 11 L12 14 C6 13.5 0.5 8 0 2Z" fill="#ec1f27"/></svg></span><span>1 888 888 8888</span></div>
<div class="info-row" style="top:3248px"><span class="info-icon"><svg width="14" height="11" viewBox="0 0 14 11"><rect width="14" height="11" rx="1.5" fill="#ec1f27"/><path d="M1 1.5 L7 6 L13 1.5" fill="none" stroke="#fff" stroke-width="1.4"/></svg></span><span>info@furlinerescue.nz</span></div>
<div class="sub-head" style="left:783px;top:3294px">Social Media</div>
<div class="socials" aria-label="Social media links">
  <span style="background:#3b5998"></span><span style="background:#1da1f2"></span><span style="background:#0e76a8"></span><span style="background:#c8232c"></span><span style="background:#dd4b39"></span>
</div>

<div class="rule"></div>
<div class="copyright">Copyright © 2018, Furline Rescue. All rights reserved.</div>

</body>
</html>
```